Quarnfield Fintech Product Infographic

Quarnfield is an established Fintech business, supplying complex financial software to banks and building societies.

We currently have a picture/infographic to show each of our 11 different software products in a single image. Each product can be installed on its own as a standalone application or if multiple products are installed they will share data.

The key message for our infographic is to convey the integration via a shared database.

The attached diagram is what we currently use which is to give you an idea of the message we are trying to give, but we are not tied to this format and are looking for this diagram to be reimagined.

We will look to use our new chosen design on printed media such as A4 Data sheets an example of which is attached.

For more information on our products please refer to www.quarnfield-example.co.uk/products

```html
<!DOCTYPE html>
<html lang="en">
<head>
<meta charset="utf-8">
<title>Quarnfield – Shared Data Product Infographic</title>
<link rel="stylesheet" href="https://fonts.googleapis.com/css2?family=Oswald:wght@500&family=Montserrat:wght@600&display=swap">
<style>
  :root {
    --canvas: #ffffff;
    --heading: #5a5a5a;
    --label: #555555;
    --hub-navy: #2a2876;
    --hub-navy-light: #3e3b9c;
    --hub-ring: #b9b9bd;
    --hub-ring-light: #e6e6e8;
    --perf-light: #ecc2df;
    --perf-dark: #7a4a9f;
    --perf-rule: #c77fb8;
    --fin-light: #9adcf5;
    --fin-dark: #1c6db5;
    --fin-rule: #4fbde8;
    --risk-light: #fbb534;
    --risk-dark: #95706e;
    --risk-rule: #f6b24a;
    --reg-light: #6cc792;
    --reg-dark: #2a6b8b;
    --reg-rule: #4fb884;
    --panel: #ffffff;
  }
  html, body {
    margin: 0;
    padding: 0;
    width: 1200px;
    height: 1200px;
    overflow: hidden;
    background: var(--canvas);
  }
  .infographic { display: block; width: 1200px; height: 1200px; }
  .section-title {
    font-family: "Oswald", "Arial Narrow", sans-serif;
    font-weight: 500;
    font-size: 19px;
    fill: var(--heading);
    text-anchor: middle;
  }
  .product-label {
    font-family: "Montserrat", Arial, sans-serif;
    font-weight: 600;
    font-size: 10.6px;
    fill: var(--label);
    text-anchor: middle;
  }
  .hub-label {
    font-family: "Oswald", "Arial Narrow", sans-serif;
    font-weight: 500;
    font-size: 24px;
    fill: #666666;
    text-anchor: middle;
    letter-spacing: 0.5px;
  }
  .panel-inner { fill: var(--panel); }
  .rule { stroke-width: 1.6; }
  .rule-performance { stroke: var(--perf-rule); }
  .rule-finance { stroke: var(--fin-rule); }
  .rule-risk { stroke: var(--risk-rule); }
  .rule-regulatory { stroke: var(--reg-rule); }
</style>
</head>
<body>
<svg class="infographic" viewBox="0 0 660 660" xmlns="http://www.w3.org/2000/svg" role="img" aria-label="Quarnfield products sharing one central database">
  <defs>
    <linearGradient id="grad-performance" x1="0" y1="0" x2="1" y2="1">
      <stop offset="0" stop-color="var(--perf-light)"/>
      <stop offset="1" stop-color="var(--perf-dark)"/>
    </linearGradient>
    <linearGradient id="grad-finance" x1="1" y1="0" x2="0" y2="1">
      <stop offset="0" stop-color="var(--fin-light)"/>
      <stop offset="1" stop-color="var(--fin-dark)"/>
    </linearGradient>
    <linearGradient id="grad-risk" x1="0" y1="0" x2="1" y2="1">
      <stop offset="0" stop-color="var(--risk-dark)"/>
      <stop offset="0.55" stop-color="var(--risk-light)"/>
      <stop offset="1" stop-color="var(--risk-light)"/>
    </linearGradient>
    <linearGradient id="grad-regulatory" x1="1" y1="0" x2="0" y2="1">
      <stop offset="0" stop-color="var(--reg-light)"/>
      <stop offset="0.5" stop-color="var(--reg-light)"/>
      <stop offset="1" stop-color="var(--reg-dark)"/>
    </linearGradient>
    <radialGradient id="grad-hub" cx="0.5" cy="0.5" r="0.6">
      <stop offset="0" stop-color="var(--hub-navy-light)"/>
      <stop offset="1" stop-color="var(--hub-navy)"/>
    </radialGradient>
    <linearGradient id="grad-hub-ring" x1="0" y1="0" x2="1" y2="1">
      <stop offset="0" stop-color="var(--hub-ring-light)"/>
      <stop offset="1" stop-color="var(--hub-ring)"/>
    </linearGradient>
    <path id="diamond-outer" d="M0,-95 C33,-95 95,-33 95,0 C95,33 33,95 0,95 C-33,95 -95,33 -95,0 C-95,-33 -33,-95 0,-95Z"/>
    <path id="diamond-inner" d="M0,-77 C27,-77 77,-27 77,0 C77,27 27,77 0,77 C-27,77 -77,27 -77,0 C-77,-27 -27,-77 0,-77Z"/>
    <clipPath id="panel-clip">
      <use href="#diamond-inner"/>
    </clipPath>
  </defs>

  <!-- Central connector -->
  <g class="hub-connector" fill="none" stroke="url(#grad-hub)">
    <line x1="330" y1="330" x2="192" y2="195" stroke-width="46"/>
    <line x1="330" y1="330" x2="467" y2="195" stroke-width="46"/>
    <line x1="330" y1="330" x2="192" y2="462" stroke-width="46"/>
    <line x1="330" y1="330" x2="467" y2="462" stroke-width="46"/>
  </g>
  <rect class="hub-body" x="262" y="262" width="136" height="136" rx="40" fill="url(#grad-hub)" transform="rotate(45 330 330)"/>

  <!-- Performance -->
  <text class="section-title" x="192" y="85">PERFORMANCE</text>
  <g class="product-group performance" transform="translate(192 195)">
    <use href="#diamond-outer" fill="url(#grad-performance)"/>
    <use href="#diamond-inner" class="panel-inner"/>
    <g clip-path="url(#panel-clip)">
      <line class="rule rule-performance" x1="-90" y1="-15" x2="90" y2="-15"/>
      <line class="rule rule-performance" x1="-90" y1="22" x2="90" y2="22"/>
    </g>
    <text class="product-label" y="-36">Financial</text>
    <text class="product-label" y="-21">Planning</text>
    <text class="product-label" y="0">Funds Transfer</text>
    <text class="product-label" y="15">Pricing</text>
    <text class="product-label" y="36">Business</text>
    <text class="product-label" y="51">Intelligence</text>
  </g>

  <!-- Finance -->
  <text class="section-title" x="462" y="85">FINANCE</text>
  <g class="product-group finance" transform="translate(467 195)">
    <use href="#diamond-outer" fill="url(#grad-finance)"/>
    <use href="#diamond-inner" class="panel-inner"/>
    <g clip-path="url(#panel-clip)">
      <line class="rule rule-finance" x1="-90" y1="-15" x2="90" y2="-15"/>
      <line class="rule rule-finance" x1="-90" y1="22" x2="90" y2="22"/>
    </g>
    <text class="product-label" x="-5" y="-36">Financial</text>
    <text class="product-label" x="-5" y="-21">Ledgers</text>
    <text class="product-label" x="-5" y="0">Effective Interest</text>
    <text class="product-label" x="-5" y="15">Rates</text>
    <text class="product-label" x="-5" y="36">Hedges</text>
    <text class="product-label" x="-5" y="51">Accounting</text>
  </g>

  <!-- Risk -->
  <g class="product-group risk" transform="translate(192 462)">
    <use href="#diamond-outer" fill="url(#grad-risk)"/>
    <use href="#diamond-inner" class="panel-inner"/>
    <g clip-path="url(#panel-clip)">
      <line class="rule rule-risk" x1="-90" y1="-5" x2="90" y2="-5"/>
    </g>
    <text class="product-label" y="-24">Treasury</text>
    <text class="product-label" y="19">ALM</text>
  </g>
  <text class="section-title" x="192" y="586">RISK</text>

  <!-- Regulatory -->
  <g class="product-group regulatory" transform="translate(467 462)">
    <use href="#diamond-outer" fill="url(#grad-regulatory)"/>
    <use href="#diamond-inner" class="panel-inner"/>
    <g clip-path="url(#panel-clip)">
      <line class="rule rule-regulatory" x1="-90" y1="-14" x2="90" y2="-14"/>
      <line class="rule rule-regulatory" x1="-90" y1="25" x2="90" y2="25"/>
    </g>
    <text class="product-label" y="-35">Regulatory</text>
    <text class="product-label" y="-20">Reporting</text>
    <text class="product-label" y="1">Taxation</text>
    <text class="product-label" y="16">Reporting</text>
    <text class="product-label" y="40">FSCS SCV</text>
  </g>
  <text class="section-title" x="465" y="586">REGULATORY</text>

  <!-- Shared data hub -->
  <g class="shared-data-hub" transform="translate(330 330)">
    <rect x="-53" y="-53" width="106" height="106" rx="22" fill="url(#grad-hub-ring)" transform="rotate(45)"/>
    <rect x="-42" y="-42" width="84" height="84" rx="16" fill="#ffffff" stroke="#d4d4d8" stroke-width="1.5" transform="rotate(45)"/>
    <text class="hub-label" y="-3">SHARED</text>
    <text class="hub-label" y="25">DATA</text>
  </g>
</svg>
</body>
</html>
```